Lorvi is a sparkling water from the Caucasian mountains.

Target Market(s)

High-end consumers

Colors

Designer to choose colors to be used in the design.

Requirements
Must have
• Sense of water from the mountines
Nice to have
• Sense of beign healing water

```html
<!DOCTYPE html>
<html lang="en">
<head>
<meta charset="utf-8">
<title>Lorvi Sparkling Water Label</title>
<link rel="stylesheet" href="https://fonts.googleapis.com/css2?family=Montserrat:wght@300;400;500&display=swap">
<style>
  :root {
    --canvas-bg: #eef2f6;
    --label-top: #5577b3;
    --label-mid: #6f90c4;
    --label-edge: #8aa6d2;
    --ice-light: #dff0f9;
    --ice-mid: #9fd0ea;
    --lake-blue: #2a9ad8;
    --mountain-blue: #5f92c2;
    --pill-blue: #2f8fd0;
    --text-white: #ffffff;
    --text-soft: #e3ecf8;
    --text-grey: #5d6670;
    --foot-bg: #e9f4fa;
  }
  * { margin: 0; padding: 0; box-sizing: border-box; }
  html, body {
    width: 740px;
    height: 1200px;
    overflow: hidden;
    background: var(--canvas-bg);
  }
  .canvas {
    position: relative;
    width: 740px;
    height: 1200px;
  }
  .label {
    position: absolute;
    left: 70px;
    top: 228px;
    width: 600px;
    height: 745px;
    overflow: hidden;
    background: linear-gradient(90deg, var(--label-edge) 0%, var(--label-mid) 18%, var(--label-top) 50%, var(--label-mid) 82%, var(--label-edge) 100%);
    box-shadow: 0 10px 30px rgba(40, 70, 110, 0.18);
  }
  .brand-block {
    position: absolute;
    left: 0;
    top: 88px;
    width: 100%;
    text-align: center;
    font-family: 'Montserrat', sans-serif;
    color: var(--text-white);
  }
  .brand-name {
    font-size: 104px;
    font-weight: 500;
    line-height: 1;
    letter-spacing: 0.02em;
  }
  .product-type {
    margin-top: 8px;
    font-size: 22px;
    font-weight: 300;
    letter-spacing: 0.36em;
    color: var(--text-soft);
    line-height: 1;
  }
  .origin-pill {
    display: inline-block;
    margin-top: 6px;
    padding: 3px 18px;
    border-radius: 12px;
    background: var(--pill-blue);
    font-size: 12px;
    font-weight: 400;
    letter-spacing: 0.02em;
    color: var(--text-white);
    line-height: 1.2;
  }
  .scene-art {
    position: absolute;
    left: 0;
    top: 0;
    width: 600px;
    height: 745px;
  }
  .volume {
    position: absolute;
    left: 0;
    bottom: 38px;
    width: 100%;
    text-align: center;
    font-family: 'Montserrat', sans-serif;
    font-size: 20px;
    font-weight: 400;
    color: var(--text-grey);
  }
</style>
</head>
<body>
<main class="canvas">
  <section class="label">
    <svg class="scene-art" viewBox="0 0 600 745" role="img" aria-label="Illustration of snowy Caucasian mountain peaks above a winding glacial lake">
      <defs>
        <linearGradient id="mountainScene" x1="0" y1="0" x2="0" y2="1">
          <stop offset="0" stop-color="#7fb2d8"/>
          <stop offset="0.35" stop-color="#b9dcef"/>
          <stop offset="0.6" stop-color="#dff0f9"/>
          <stop offset="0.8" stop-color="#62b6e4"/>
          <stop offset="1" stop-color="#e9f4fa"/>
        </linearGradient>
      </defs>
      <path d="M0 300 L0 745 L600 745 L600 300 Q300 270 0 300 Z" fill="url(#mountainScene)"/>
    </svg>
    <div class="brand-block">
      <h1 class="brand-name">LORVI</h1>
      <p class="product-type">SPARKLING WATER</p>
      <p class="origin-pill">FROM THE CAUCASIAN MOUNTAINS</p>
    </div>
    <p class="volume">500 ml</p>
  </section>
</main>
</body>
</html>
```